Talvoro bonds (Surety bond broker)

We are a broker of surety bonds, we need a presentation and a flyer with fresh design. Our core values are reliable, on time and customized service. We want to transmit to our clients, they can leave on us the process of underwriting and issuing a surety bond, so they can focus on their business with no distractions.

Font styles to use
Sans Serif
Other font styles liked:

Requirements
Must have
• Visually attractive.
Main Message: Fast service issuing and underwriting surety bonds, reliable, nos surprises, we are always one step ahead, customized and personalized bonding solutions.
Nice to have
• Have short version for the flyer, and extended version for the presentation.
Should not have
• We already have a logo (attached), maintain colors

```html
<!DOCTYPE html>
<html lang="es">
<head>
<meta charset="utf-8">
<title>Talvoro – Presentación</title>
<link href="https://fonts.googleapis.com/css2?family=Open+Sans:wght@400;600;700&display=swap" rel="stylesheet">
<style>
:root{
  --bg-top:#8f8f8f;
  --bg-bottom:#7b7b7b;
  --slide:#4b4b4b;
  --white:#ffffff;
  --ink:#333333;
  --muted:#d9d9d9;
  --green:#7ac143;
  --green-soft:rgba(122,193,67,.75);
  --grey-node:#9a9a9a;
}
*{box-sizing:border-box;margin:0;padding:0}
html,body{width:1200px;height:585px;overflow:hidden}
body{background:linear-gradient(160deg,var(--bg-top),var(--bg-bottom));font-family:"Open Sans",Arial,sans-serif;color:var(--white)}
.board{position:relative;width:2576px;height:1255px;transform:scale(.46584);transform-origin:0 0}
.slide{position:absolute;width:557px;height:313px;background:var(--slide);overflow:hidden}
.slide--light{background:var(--white);color:var(--ink)}
.title{position:absolute;left:46px;top:28px;font-size:17px;font-weight:700;letter-spacing:.2px;white-space:nowrap}
.title em{font-style:normal;color:var(--green)}
.dash{position:absolute;left:46px;top:60px;width:12px;height:2px;background:var(--green)}
.photo{position:absolute;border-radius:50%}
.ring{position:absolute;border-radius:50%;border:1.5px solid var(--green)}
.dot{position:absolute;border-radius:50%;background:var(--green-soft)}
.foot{position:absolute;left:0;top:0;width:557px;height:313px;pointer-events:none}
.web{position:absolute;left:46px;top:290px;font-size:6.5px;letter-spacing:1.6px;font-weight:600}
.web b{color:var(--green);font-weight:600}
.brand{position:absolute;left:446px;top:284px;font-size:10px;font-weight:400;color:var(--green);letter-spacing:.5px}
.page{position:absolute;left:515px;top:285px;width:11px;height:11px;border-radius:50%;background:var(--white);color:var(--slide);font-size:7px;font-weight:700;text-align:center;line-height:11px}
.slide--light .page{background:var(--ink);color:var(--white)}
.body{position:absolute;left:46px;width:232px;font-size:5.8px;line-height:1.7;text-align:justify;color:var(--muted)}
.body p{margin-bottom:10px}
.body .lead{color:var(--green);font-weight:600}
.body h4{font-size:7px;font-weight:600;color:var(--green);margin:6px 0 3px}
.cover-brand{position:absolute;left:36px;top:36px;font-size:30px;font-weight:400;color:var(--green);letter-spacing:1px}
.cover-head{position:absolute;left:36px;top:160px;font-size:24px;font-weight:700;line-height:1.25}
.cover-head em{font-style:normal;color:var(--green)}
.cover-web{position:absolute;left:36px;top:266px;font-size:11px;letter-spacing:2.4px;font-weight:600}
.index-list{position:absolute;left:110px;top:72px;list-style:none;font-size:7px;color:var(--ink)}
.index-list li{height:18.6px;display:flex;align-items:center;gap:8px}
.index-list i{display:inline-block;width:9px;height:9px;border-radius:50%;background:var(--green);color:var(--white);font-style:normal;font-size:5.5px;font-weight:700;text-align:center;line-height:9px}
.checks{position:absolute;left:46px;top:80px;width:240px;list-style:none;font-size:7px;line-height:1.35}
.checks li{position:relative;padding-left:13px;margin-bottom:9px}
.checks li::before{content:"";position:absolute;left:1px;top:1px;width:3px;height:6px;border:solid var(--green);border-width:0 1.2px 1.2px 0;transform:rotate(40deg)}
.checks small{display:block;font-size:4.6px;color:#bdbdbd}
.prod{position:absolute;width:58px;height:58px;border-radius:50%;background:var(--green);border:2px solid var(--white);box-shadow:0 0 0 1.5px var(--green);display:flex;flex-direction:column;align-items:center;justify-content:flex-end;padding-bottom:10px;font-size:5px;font-weight:600}
.prod svg{margin-bottom:4px}
.plist{position:absolute;font-size:5px;line-height:1.55;color:#cfcfcf;list-style:none}
.plist .g{color:var(--green)}
.tile{position:absolute;width:135px;height:56px;background:var(--white);display:flex;align-items:center;justify-content:center}
.contact{position:absolute;left:46px;font-size:8px;line-height:1.6}
.contact .name{color:var(--green);font-weight:600;font-size:8.5px;padding-left:18px}
.contact .row{display:flex;align-items:center;gap:6px}
.contact .row i{display:inline-block;width:10px;height:10px;border-radius:50%;border:1px solid #777}
.node{position:absolute;border-radius:50%;display:flex;align-items:center;justify-content:center;text-align:center;font-size:3.8px;font-weight:700;line-height:1.25;color:var(--white);padding:4px}
.node--green{background:var(--green)}
.node--grey{background:var(--grey-node)}
.node--black{background:#111}
</style>
</head>
<body>
<div class="board">

<section class="slide" style="left:77px;top:89px">
  <div class="cover-brand">TALVORO</div>
  <h1 class="cover-head">Tu éxito<br><em>Nuestra pasión</em></h1>
  <div class="dash" style="left:36px;top:232px;width:22px"></div>
  <div class="cover-web">www.talvoro.com</div>
  <div class="ring" style="left:228px;top:-14px;width:318px;height:318px"></div>
  <div class="photo" role="img" aria-label="Collage fotográfico: obrero con casco amarillo, edificios y vías urbanas" style="left:238px;top:-6px;width:298px;height:298px;background:radial-gradient(circle at 45% 45%,#f4d27a 0%,#c89b52 22%,#6d7d93 55%,#dfe3e8 100%)"></div>
</section>

<section class="slide" style="left:677px;top:89px">
  <div class="photo" role="img" aria-label="Fondo tenue de ciudad en construcción con grúas" style="left:200px;top:-40px;width:420px;height:360px;border-radius:0;background:linear-gradient(90deg,rgba(75,75,75,0),#5a5d60 70%,#4e5154)"></div>
  <div class="ring" style="left:38px;top:-62px;width:300px;height:300px"></div>
  <div class="photo" style="left:43px;top:-57px;width:290px;height:290px;background:var(--white)"></div>
  <div class="title" style="left:127px;top:30px;color:var(--green);font-weight:600">Índice</div>
  <div class="dash" style="left:128px;top:55px;width:6px"></div>
  <ol class="index-list">
    <li><i>1</i>¿Quiénes somos?</li>
    <li><i>2</i>Oferta de Valor</li>
    <li><i>3</i>Nuestros Servicios</li>
    <li><i>4</i>Productos</li>
    <li><i>5</i>Ciclo de administración de Fianzas</li>
    <li><i>6</i>Nuestros socios de negocio</li>
    <li><i>7</i>Contacto</li>
  </ol>
  <svg class="foot" viewBox="0 0 557 313"><path d="M118 296H418L436 280H500" fill="none" stroke="#7ac143" stroke-width=".8"/></svg>
  <div class="web">www.<b>talvoro</b>.com</div><div class="brand">TALVORO</div><div class="page">2</div>
</section>

<section class="slide" style="left:1288px;top:89px">
  <div class="title">¿Quiénes <em>somos?</em></div><div class="dash"></div>
  <div class="body" style="top:80px">
    <p>Somos un grupo de jóvenes emprendedores, con amplia experiencia en el sector afianzador.</p>
    <p>Estamos convencidos de que nuestro principal diferenciador es la pasión por el servicio.</p>
    <p>Nuestra prioridad es el éxito de cada uno de nuestros clientes, nos aseguramos de que el "trámite" de fianzas deje de ser un "trámite" y se convierta en la llave al éxito para cada uno de nuestros fiados y beneficiarios.</p>
    <p>Buscamos siempre tener relaciones estrechas y de largo plazo con todos nuestros "stakeholders". Por lo que nos rodeamos del mejor talento en el sector para garantizar a nuestros clientes un servicio personalizado, en tiempo y confiable.</p>
  </div>
  <div class="ring" style="left:306px;top:-42px;width:300px;height:300px"></div>
  <div class="photo" role="img" aria-label="Fotografía de obra en construcción con grúa amarilla al atardecer" style="left:312px;top:-36px;width:290px;height:290px;background:linear-gradient(160deg,#2f8fd0 0%,#9cc6de 35%,#e9b24a 60%,#6d5b45 100%)"></div>
  <div class="dot" style="left:320px;top:190px;width:44px;height:44px"></div>
  <div class="dot" style="left:358px;top:222px;width:24px;height:24px"></div>
  <svg class="foot" viewBox="0 0 557 313"><path d="M118 296H418L436 280H500" fill="none" stroke="#7ac143" stroke-width=".8"/></svg>
  <div class="web">www.<b>talvoro</b>.com</div><div class="brand">TALVORO</div><div class="page">3</div>
</section>

<section class="slide" style="left:1899px;top:89px">
  <div class="title">Nuestra oferta <em>de valor</em></div><div class="dash"></div>
  <div class="body" style="top:78px">
    <p><span class="lead">Para nuestros fiados,</span><br>nos aseguramos de que el proceso de emisión de fianzas sea <span class="lead">claro, rápido y sencillo.</span> Dando una asesoría personalizada y seguimiento puntual a cada solicitud.</p>
    <p>Sabemos la importancia de tener una fianza en tiempo y sin errores, por lo que nos empeñamos en siempre ir un paso adelante, permitiendo que nuestros clientes se despreocupen del proceso de afianzamiento y logren todos sus objetivos.</p>
    <p><span class="lead">Para nuestros beneficiarios,</span><br>trabajamos solo con las mejores afianzadoras del país y garantizamos que todos nuestros clientes cuenten con una garantía confiable, que les permita concluir sus proyectos con la tranquilidad de que tienen un respaldo confiable. Nuestro compromiso es siempre mitigar los riesgos y nunca dejar desprotegidos a nuestros clientes.</p>
  </div>
  <div class="ring" style="left:300px;top:-42px;width:300px;height:300px"></div>
  <div class="photo" role="img" aria-label="Fotografía de obreros en silueta sobre andamio al atardecer" style="left:306px;top:-36px;width:290px;height:290px;background:linear-gradient(180deg,#6aa9d6 0%,#c8d7df 40%,#f0a64e 65%,#2c2c2c 100%)"></div>
  <div class="dot" style="left:318px;top:188px;width:44px;height:44px"></div>
  <div class="dot" style="left:356px;top:220px;width:24px;height:24px"></div>
  <svg class="foot" viewBox="0 0 557 313"><path d="M118 296H418L436 280H500" fill="none" stroke="#7ac143" stroke-width=".8"/></svg>
  <div class="web">www.<b>talvoro</b>.com</div><div class="brand">TALVORO</div><div class="page">4</div>
</section>

<section class="slide" style="left:77px;top:467px">
  <div class="title">Nuestros <em>Servicios</em></div><div class="dash"></div>
  <ul class="checks">
    <li>Asesoría personalizada para la obtención de Líneas de Afianzamiento</li>
    <li>Emisión y administración de fianzas.<small>(Fidelidad, Administrativas, Judiciales, Crédito y Fideicomisos)</small></li>
    <li>Diseño, implementación y gestión de esquemas de afianzamiento.</li>
    <li>Asesoría en riesgos para contratos de obra, suministro y proveeduría.</li>
    <li>Colocación de fianzas internacionales y reaseguro.</li>
    <li>Asesoría legal en proceso de reclamación de fianzas.</li>
    <li>Esquemas de afianzamiento masivos.</li>
  </ul>
  <div class="ring" style="left:300px;top:-40px;width:290px;height:290px"></div>
  <div class="photo" role="img" aria-label="Fotografía de casco de obra azul frente a edificios" style="left:306px;top:-34px;width:280px;height:280px;background:linear-gradient(135deg,#e8eef3 0%,#6a93b8 40%,#1f4e79 65%,#e07a3a 100%)"></div>
  <div class="dot" style="left:320px;top:188px;width:44px;height:44px"></div>
  <div class="dot" style="left:356px;top:220px;width:24px;height:24px"></div>
  <svg class="foot" viewBox="0 0 557 313"><path d="M118 296H418L436 280H500" fill="none" stroke="#7ac143" stroke-width=".8"/></svg>
  <div class="web">www.<b>talvoro</b>.com</div><div class="brand">TALVORO</div><div class="page">5</div>
</section>

<section class="slide" style="left:677px;top:467px">
  <div class="title">Productos <em>en Fianzas</em></div><div class="dash"></div>
  <svg class="foot" viewBox="0 0 557 313">
    <g fill="none" stroke="#7ac143" stroke-width=".8">
      <path d="M156 137V155H65"/><path d="M258 137V155H340"/>
      <path d="M156 234V252H65"/><path d="M258 234V252H340"/>
      <path d="M118 296H418L436 280H500"/>
    </g>
    <g fill="#7ac143"><circle cx="65" cy="155" r="1.5"/><circle cx="340" cy="155" r="1.5"/><circle cx="65" cy="252" r="1.5"/><circle cx="340" cy="252" r="1.5"/></g>
    <g stroke="#888" stroke-width=".6"><path d="M405 86V128"/><path d="M405 190V220"/></g>
  </svg>
  <div class="prod" style="left:127px;top:79px"><svg width="16" height="16" viewBox="0 0 16 16"><circle cx="9" cy="3" r="2" fill="#fff"/><path d="M5 15L8 9L11 12V15M8 9L6 6H10L12 8" stroke="#fff" stroke-width="1.6" fill="none" stroke-linecap="round"/></svg>Fidelidad</div>
  <div class="prod" style="left:229px;top:79px"><svg width="16" height="16" viewBox="0 0 16 16"><path d="M6 2L11 7M4 4L9 9M7 6L13 12" stroke="#fff" stroke-width="2" stroke-linecap="round"/><rect x="2" y="13" width="8" height="2" fill="#fff"/></svg>Judicial</div>
  <div class="prod" style="left:127px;top:176px"><svg width="18" height="14" viewBox="0 0 18 14"><rect x="1" y="2" width="16" height="10" rx="1.5" fill="none" stroke="#fff" stroke-width="1.3"/><path d="M1 5H17" stroke="#fff" stroke-width="1.3"/><path d="M4 9H9" stroke="#fff"/></svg>Crédito</div>
  <div class="prod" style="left:229px;top:176px"><svg width="16" height="16" viewBox="0 0 16 16"><circle cx="8" cy="5" r="3" fill="none" stroke="#fff" stroke-width="1.3"/><path d="M2 15C2 11 5 9 8 9S14 11 14 15Z" fill="none" stroke="#fff" stroke-width="1.3"/></svg>Administrativas</div>
  <ul class="plist" style="left:46px;top:100px"><li class="g">✓ Colectiva</li><li class="g">✓ Individual</li></ul>
  <ul class="plist" style="left:308px;top:86px"><li class="g">✓ Penales</li><li>• Libertad provisional</li><li>• Condena provisional</li><li>• Reparación del daño</li><li>• Sanción pecuniaria</li></ul>
  <ul class="plist" style="left:410px;top:86px"><li class="g">✓ No Penales</li><li>• Daños y perjuicios</li><li>• Pensión alimenticia</li><li>• Laboral</li></ul>
  <ul class="plist" style="left:46px;top:176px"><li class="g">✓ Compra venta</li><li class="g">✓ Suministro</li><li>• CLVQ</li><li>• Estaciones de Servicio</li><li>• PTRX</li><li>• AVQZ</li><li class="g">✓ Otras Crédito</li></ul>
  <ul class="plist" style="left:308px;top:184px"><li class="g">✓ Obra y Proveeduría</li><li>• Cumplimiento</li><li>• Anticipo</li><li>• Buena Calidad</li><li>• Contingencias Laborales</li></ul>
  <ul class="plist" style="left:410px;top:194px"><li class="g">✓ Arrendamiento</li><li class="g">✓ Contingencias ambientales</li><li class="g">✓ Fiscales</li></ul>
  <div class="web">www.<b>talvoro</b>.com</div><div class="brand">TALVORO</div><div class="page">6</div>
</section>

<section class="slide" style="left:1288px;top:467px">
  <div class="title">Productos <em>Especiales</em></div><div class="dash"></div>
  <div class="body" style="top:72px;font-size:4.6px;line-height:1.55;color:#c4c4c4">
    <h4>Flujo Garantizado</h4>
    <p>Es una fianza con la que se constituye un fondo colectivo para productos masivos que permite dar visibilidad financiera a tu empresa, proporcionándole el flujo constante de recursos para cubrir posibles pérdidas por quebrantos de créditos o cuentas por cobrar no liquidadas por sus clientes.</p>
    <h4>Esquemas de Proveedores</h4>
    <p>Esquema diseñado para grandes beneficiarios, que permite proteger los recursos invertidos en proyectos de construcción y adquisición de bienes o prestación de servicios, garantizando las obligaciones que se derivan de estos a cargo de sus proveedores o contratistas.</p>
    <p>Este programa permite la fácil administración de fianzas, proveniendo un procedimiento ágil para la ejecución y cobro de las garantías que se emitan dentro del esquema.</p>
    <h4>Programa de garantías de fianzas para PyMEs</h4>
    <p>Con este programa puedes incrementar la línea de afianzamiento, gracias a que un fondo público aporta el 50% de las garantías requeridas en fianzas hasta por 30 millones de pesos.</p>
  </div>
  <div class="ring" style="left:306px;top:-42px;width:300px;height:300px"></div>
  <div class="photo" role="img" aria-label="Fotografía aérea de rascacielos de una gran ciudad" style="left:312px;top:-36px;width:290px;height:290px;background:linear-gradient(180deg,#dfe8ef 0%,#9fb4c6 40%,#3e5870 70%,#22303d 100%)"></div>
  <div class="dot" style="left:320px;top:188px;width:44px;height:44px"></div>
  <div class="dot" style="left:358px;top:220px;width:24px;height:24px"></div>
  <svg class="foot" viewBox="0 0 557 313"><path d="M118 296H418L436 280H500" fill="none" stroke="#7ac143" stroke-width=".8"/></svg>
  <div class="web">www.<b>talvoro</b>.com</div><div class="brand">TALVORO</div><div class="page">7</div>
</section>

<section class="slide slide--light" style="left:1888px;top:467px">
  <div class="title" style="color:var(--ink)">Ciclo de <em>administración de Fianzas</em></div><div class="dash"></div>
  <svg class="foot" viewBox="0 0 557 313">
    <circle cx="279" cy="170" r="76" fill="none" stroke="#444" stroke-width="6"/>
    <path d="M222 117L240 100" stroke="#444" stroke-width="6"/>
    <path d="M234 92L250 90L246 106Z" fill="#444"/>
    <circle cx="279" cy="170" r="23" fill="none" stroke="#333" stroke-width="1.4"/>
    <path d="M118 296H418L436 280H500" fill="none" stroke="#7ac143" stroke-width=".8"/>
  </svg>
  <div class="node node--green" style="left:256px;top:70px;width:46px;height:46px">Alta del cliente<br><span style="font-weight:400;opacity:.8">Expediente de fiado</span></div>
  <div class="node node--grey" style="left:328px;top:100px;width:48px;height:48px">Análisis de la obligación a garantizar</div>
  <div class="node node--black" style="left:333px;top:170px;width:48px;height:48px">Integración de Garantías</div>
  <div class="node node--green" style="left:293px;top:226px;width:48px;height:48px">Autorización de Línea de Afianzamiento</div>
  <div class="node node--green" style="left:217px;top:226px;width:48px;height:48px">Emisión de Fianza</div>
  <div class="node node--black" style="left:177px;top:170px;width:48px;height:48px">Endosos de cambio Prórrogas Renovaciones</div>
  <div class="node node--grey" style="left:183px;top:100px;width:48px;height:48px">Administración de cúmulos</div>
  <div class="web" style="color:var(--ink)">www.<b>talvoro</b>.com</div><div class="brand">TALVORO</div><div class="page">8</div>
</section>

<section class="slide" style="left:77px;top:849px">
  <div class="title">Nuestro Socios <em>de Negocio</em></div><div class="dash"></div>
  <div class="tile" style="left:46px;top:78px"><svg width="90" height="24"><circle cx="12" cy="12" r="11" fill="#2a63b0"/><rect x="30" y="8" width="56" height="8" rx="2" fill="#2a63b0"/></svg></div>
  <div class="tile" style="left:197px;top:78px"><svg width="90" height="24"><circle cx="12" cy="12" r="10" fill="#e68a1e"/><rect x="28" y="7" width="58" height="10" rx="2" fill="#555"/></svg></div>
  <div class="tile" style="left:348px;top:78px"><svg width="90" height="24"><circle cx="12" cy="12" r="11" fill="#1f6db5"/><rect x="30" y="8" width="56" height="8" rx="2" fill="#444"/></svg></div>
  <div class="tile" style="left:46px;top:141px"><svg width="90" height="14"><rect x="0" y="3" width="90" height="8" rx="1" fill="#222"/></svg></div>
  <div class="tile" style="left:197px;top:141px"><svg width="90" height="30"><circle cx="15" cy="15" r="14" fill="none" stroke="#3b5a7a" stroke-width="2"/><rect x="36" y="10" width="50" height="10" rx="2" fill="#3b5a7a"/></svg></div>
  <div class="tile" style="left:348px;top:141px"><svg width="90" height="24"><rect x="8" y="8" width="74" height="12" rx="2" fill="#d21f26"/></svg></div>
  <div class="tile" style="left:46px;top:205px"><svg width="90" height="34"><rect x="2" y="2" width="22" height="30" rx="2" fill="#1b3a6b"/><rect x="32" y="12" width="54" height="10" rx="2" fill="#1b3a6b"/></svg></div>
  <div class="tile" style="left:197px;top:205px"><svg width="90" height="34"><rect x="2" y="12" width="46" height="10" rx="2" fill="#203f7a"/><circle cx="70" cy="17" r="15" fill="#203f7a"/></svg></div>
  <div class="tile" style="left:348px;top:205px"><svg width="90" height="24"><rect x="4" y="8" width="72" height="10" rx="2" fill="#444"/><circle cx="84" cy="8" r="5" fill="#d21f26"/></svg></div>
  <svg class="foot" viewBox="0 0 557 313"><path d="M118 296H418L436 280H500" fill="none" stroke="#7ac143" stroke-width=".8"/></svg>
  <div class="web">www.<b>talvoro</b>.com</div><div class="brand">TALVORO</div><div class="page">9</div>
</section>

<section class="slide" style="left:677px;top:849px">
  <div class="title">Contacto</div><div class="dash"></div>
  <div class="contact" style="top:84px">
    <div class="name">Marta Quiroga</div>
    <div class="row"><i></i>mquiroga@talvoro.com</div>
    <div class="row"><i></i>55 0100 2231</div>
  </div>
  <div class="contact" style="top:145px">
    <div class="name">Lucía Andrade</div>
    <div class="row"><i></i>landrade@talvoro.com</div>
    <div class="row"><i></i>55 0100 4472</div>
  </div>
  <div class="contact" style="top:206px">
    <div class="name">Tomás Beltrán</div>
    <div class="row"><i></i>tbeltran@talvoro.com</div>
    <div class="row"><i></i>55 0100 6815</div>
  </div>
  <div class="ring" style="left:222px;top:-12px;width:290px;height:290px"></div>
  <div class="photo" role="img" aria-label="Fotografía de apretón de manos de ejecutivos sobre fondo de ciudad" style="left:228px;top:-6px;width:278px;height:278px;background:linear-gradient(135deg,#eef3f7 0%,#8fb0cf 35%,#2d4f73 60%,#d9a06f 100%)"></div>
  <div class="dot" style="left:236px;top:192px;width:44px;height:44px"></div>
  <div class="dot" style="left:274px;top:226px;width:24px;height:24px"></div>
  <svg class="foot" viewBox="0 0 557 313"><path d="M118 296H418L436 280H500" fill="none" stroke="#7ac143" stroke-width=".8"/></svg>
  <div class="web">www.<b>talvoro</b>.com</div><div class="brand">TALVORO</div><div class="page">10</div>
</section>

</div>
</body>
</html>
```